Kestrelmoor Advisory Services LLC
The Quiet Hand Consutants
Project: Kestrelmoor Advisory Services LLC
Kestrelmoor Advisory Services LLC - Financial Services
Creative Brief
Professional
Warrick Dunstan Hollowell
Senior Managing Director
388 West 19th Street New York, N.T. 10024
whollowell@kmaservices.net
KESTRELMOORADVISORYSERVICES.COM

```html
<!DOCTYPE html>
<html lang="en">
<head>
<meta charset="utf-8">
<title>Kestrelmoor Advisory Services – Business Card</title>
<link href="https://fonts.googleapis.com/css2?family=Caladea:wght@400;700&display=swap" rel="stylesheet">
<style>
  :root {
    --backdrop: #e9e6e1;
    --card: #ffffff;
    --blue: #1f62b8;
    --blue-light: #5aa2ea;
    --blue-deep: #134a93;
    --gold: #b38a1e;
    --ink: #3a3a3a;
  }
  * { box-sizing: border-box; margin: 0; padding: 0; }
  html, body {
    width: 1200px; height: 780px; overflow: hidden;
    background: var(--backdrop);
    font-family: "Caladea", Georgia, serif;
  }
  .card {
    position: absolute; left: 100px; top: 104px;
    width: 1000px; height: 572px;
    background: var(--card);
    border-radius: 26px;
    overflow: hidden;
    box-shadow: 0 10px 30px rgba(0,0,0,0.18);
  }
  .accent-left {
    position: absolute; left: 0; top: 0; bottom: 0; width: 110px;
    background: linear-gradient(180deg, var(--blue-light), var(--blue) 55%, var(--blue-deep));
  }
  .accent-corner {
    position: absolute; right: 0; top: 0; width: 240px; height: 56px;
    background: linear-gradient(90deg, var(--blue-light), var(--blue-deep));
  }
  .panel-edge {
    position: absolute; left: 440px; top: 40px; bottom: 0; width: 28px;
    background: linear-gradient(90deg, rgba(201,204,211,0.7), rgba(255,255,255,0));
  }
  .brand {
    position: absolute; left: 130px; top: 250px; width: 300px;
    text-align: center;
    color: var(--blue);
    font-weight: 400;
    font-size: 30px; line-height: 1.15; letter-spacing: 1px;
    text-transform: uppercase;
  }
  .contact {
    position: absolute; left: 488px; top: 90px; width: 490px;
    color: var(--ink);
  }
  .contact-name { color: var(--blue); font-weight: 700; font-size: 30px; line-height: 1.1; }
  .contact-title { color: var(--gold); font-weight: 700; font-size: 21px; margin-top: 2px; }
  .contact-address { font-size: 22px; line-height: 1.2; margin-top: 34px; }
  .contact-list { list-style: none; margin-top: 22px; }
  .contact-list li {
    display: flex; align-items: center; gap: 14px;
    font-size: 20px; line-height: 31px;
  }
  .contact-list svg { width: 20px; height: 20px; flex: none; fill: var(--blue); }
</style>
</head>
<body>
  <div class="card">
    <div class="accent-left" role="img" aria-label="Blue and gold decorative band along the left edge"></div>
    <div class="accent-corner" role="img" aria-label="Blue and gold decorative band at the top right corner"></div>
    <div class="panel-edge"></div>

    <div class="brand">Kestrelmoor<br>Advisory Services</div>

    <div class="contact">
      <div class="contact-name">Warrick Dunstan Hollowell</div>
      <div class="contact-title">Senior Managing Director</div>
      <div class="contact-address">388 West 19th Street<br>New York, N.T. 10024</div>
      <ul class="contact-list">
        <li><svg viewBox="0 0 24 24"><path d="M6.6 10.8a15 15 0 0 0 6.6 6.6l2.2-2.2a1 1 0 0 1 1-.25 11.4 11.4 0 0 0 3.6.57 1 1 0 0 1 1 1V20a1 1 0 0 1-1 1A17 17 0 0 1 3 4a1 1 0 0 1 1-1h3.5a1 1 0 0 1 1 1c0 1.25.2 2.45.57 3.57a1 1 0 0 1-.25 1z"/></svg>646-555-0142</li>
        <li><svg viewBox="0 0 24 24"><rect x="7" y="2" width="10" height="20" rx="2"/><rect x="9" y="5" width="6" height="10" fill="#fff"/></svg>201-555-0187</li>
        <li><svg viewBox="0 0 24 24"><path d="M5 8h14v12H5z"/><path d="M8 3h8v5H8z"/></svg>917-555-0163</li>
        <li><svg viewBox="0 0 24 24"><circle cx="12" cy="12" r="10"/><circle cx="12" cy="12" r="4" fill="#fff"/></svg>whollowell@kmaservices.net</li>
        <li><svg viewBox="0 0 24 24"><circle cx="12" cy="12" r="10"/><path d="M2 12h20M12 2v20" stroke="#fff" stroke-width="1.5"/></svg>kestrelmooradvisoryservices.com</li>
      </ul>
    </div>
  </div>
</body>
</html>
```